International Fundraising Consultancy needs a new PowerPoint Design

We train international nonprofits on how to fundraise globally. We plan to keep our current logo design and color, as we love the color orange, but want a cleaner, fresher, less cluttered template for our PowerPoint presentations. The finished product needs to be easy to edit, and include template slides that can feature tables, graphics and images. We would like a color scheme for graphics.The layout should be lighter, clear, attractive and easy to read and understand. We also want to use the same template for webinar slides. We have attached an example of our current PowerPoint template with identifying client information removed. The green slide that looks like a clapperboard fro a film is basically just a placeholder that indicates a break for an interactive exercise.

Target Market(s)

Board members, staff members, museum executives, leadership of NGOs, top businesspeople in Europe, many with a modern sense of aesthetics in the art world

Industry/Entity Type

Cleaner

Font styles to use
Sans Serif

Colors
f78f20
f37022

Requirements
Must have
• Orange colors, keep our Vormelinck logo
• Good templates for tables, photos and graphics

```html
<!DOCTYPE html>
<html lang="en">
<head>
<meta charset="utf-8">
<title>Project Title Slide</title>
<link rel="stylesheet" href="https://fonts.googleapis.com/css2?family=Roboto+Condensed:wght@400;700&display=swap">
<style>
  :root {
    --bar: #454545;
    --orange: #f78f20;
    --orange-soft: #f8a050;
    --body-grey: #7a7a7a;
    --white: #ffffff;
    --canvas: #ffffff;
  }
  * { margin: 0; padding: 0; box-sizing: border-box; }
  html, body {
    width: 1200px;
    height: 900px;
    overflow: hidden;
    background: var(--canvas);
  }
  .slide {
    position: relative;
    width: 1200px;
    height: 900px;
    background: var(--canvas);
    font-family: "Roboto Condensed", "Arial Narrow", sans-serif;
  }
  .title-bar {
    position: absolute;
    left: 0; top: 0;
    width: 100%;
    height: 112px;
    background: var(--bar);
  }
  .slide-title {
    position: absolute;
    left: 27px;
    top: 26px;
    color: var(--white);
    font-weight: 700;
    font-size: 48px;
    line-height: 1;
    letter-spacing: 0.3px;
  }
  .content-block {
    position: absolute;
    width: 540px;
  }
  .block-heading {
    color: var(--orange-soft);
    font-weight: 700;
    font-size: 27.5px;
    line-height: 1;
    margin-bottom: 9px;
    text-transform: uppercase;
  }
  .block-text {
    color: var(--body-grey);
    font-size: 23.5px;
    line-height: 39px;
    white-space: nowrap;
  }
  .block-a { left: 66px;  top: 195px; }
  .block-b { left: 652px; top: 195px; }
  .block-c { left: 66px;  top: 466px; }
  .block-d { left: 652px; top: 466px; }

  .footer-bar {
    position: absolute;
    left: 0; bottom: 0;
    width: 100%;
    height: 65px;
    background: var(--bar);
  }
  .page-number {
    position: absolute;
    left: 0; top: 15px;
    width: 50px;
    height: 39px;
    background: var(--orange);
    color: var(--bar);
    font-size: 22px;
    line-height: 39px;
    text-align: center;
  }
  .copyright {
    position: absolute;
    left: 66px;
    top: 23px;
    color: var(--white);
    font-weight: 700;
    font-size: 19px;
    line-height: 1;
  }
  .brand-name {
    position: absolute;
    right: 10px;
    top: 23px;
    color: var(--white);
    font-size: 17px;
    line-height: 1;
  }
</style>
</head>
<body>
  <main class="slide">
    <header class="title-bar">
      <h1 class="slide-title">PROJECT TITLE HERE</h1>
    </header>

    <section class="content-block block-a">
      <h2 class="block-heading">Subtext here subtext here</h2>
      <p class="block-text">Subtext here Subtext here Subtext here Subtext<br>here&nbsp; Subtext here Subtext here&nbsp; Subtext here<br>Subtext here&nbsp; Subtext here Subtext here Subtext<br>here Subtext here&nbsp; Subtext here Subtext here</p>
    </section>

    <section class="content-block block-b">
      <h2 class="block-heading">Subtext here subtext here</h2>
      <p class="block-text">Subtext here Subtext here Subtext here Subtext<br>here&nbsp; Subtext here Subtext here&nbsp; Subtext here<br>Subtext here&nbsp; Subtext here Subtext here Subtext<br>here Subtext here&nbsp; Subtext here Subtext here</p>
    </section>

    <section class="content-block block-c">
      <h2 class="block-heading">Subtext here subtext here</h2>
      <p class="block-text">Subtext here Subtext here Subtext here Subtext<br>here&nbsp; Subtext here Subtext here&nbsp; Subtext here<br>Subtext here&nbsp; Subtext here Subtext here Subtext<br>here Subtext here&nbsp; Subtext here Subtext here</p>
    </section>

    <section class="content-block block-d">
      <h2 class="block-heading">Subtext here subtext here</h2>
      <p class="block-text">Subtext here Subtext here Subtext here Subtext<br>here&nbsp; Subtext here Subtext here&nbsp; Subtext here<br>Subtext here&nbsp; Subtext here Subtext here Subtext<br>here Subtext here&nbsp; Subtext here Subtext here</p>
    </section>

    <footer class="footer-bar">
      <div class="page-number">01</div>
      <p class="copyright">Copyright text here</p>
      <p class="brand-name">Vormelinck</p>
    </footer>
  </main>
</body>
</html>
```